Elegant and modern body scrub for organic junkies

I need a package design for my new company based out of Austin, Texas. We are focused on cruelty free and all natural and organic products. Our deign needs to be able to have the information we require on it, while still appearing very clean and captivating. Our initial product is a clear skin body scrub, intended for people with problematic skin. Our target market is women and we want to show elegance, without appearing "high end."
Updates

Reason: I want to allot more time for certain designers to submit edits. Last minute proposals have been appealing

Target Market(s)

Women. Organic and holistic minded. Natural beauty lovers.

Industry/Entity Type

Skin Care Product

Font styles to use
Script
Other font styles liked:
• AmericanTypewriter, Beautifulflaws, courier, caviarDreams-bold

Colors
000000
ffc214
ffffff
fece3e
fbee3e

Requirements
Must have
• Must be designed in Adobe Illustrator.
• The photo titled “structure for oz and grams” -That needs to be included at the bottom of 1B. I like the horizontal and vertical bar that separate the two. I want that.
• Color Inspiration - The photo titled “vorna color inspiration” and “color combo inspiration” are the colors I want. BLACK, GOLD, WHITE. I want the label background black and the writing in white with some gold somewhere on it. My logo is going to be a Saffron Meadow.
• The photos titled “I like how clean this looks” and “I also like how clean this looks” - I want 1B to look super clean. I don’t want a lot of information in this box. I want simple and clean. This is where the logo and brand name will go.
• Logo - A Saffron Meadow. I want it to be gold and geometric. There can be dimension like this elephant example on the left of the 1B description. I want the trunk to be facing to the left and the trunk needs to be raised overhead and touching the animal's forehead.
• The photo titled “sideways writing and silver rim” - I want 1C to be written sideways like this. My text will be much more extensive so the font won’t be able to be so big.
Nice to have
• The photo titled “sideways writing and silver rim” - I want 1C to be written sideways like this. My text will be much more extensive so the font won’t be able to be so big. I also REALLY like how this label is rimmed in silver, but I would want gold. This is not mandatory, but I really like this.
• The photo titled “melted honey” - This is another option I really like. The gold that looks like honey dripping on the label is really cool. Not mandatory, but I really liked that. I also like the craft background on this.
• Color Inspiration - The photo titled “color inspiration” and “another color inspiration” is an option I would also like to see. Rather than black, I’d like to see what it would ALSO look like with a navy background. NAVY, GOLD, WHITE, maybe black somewhere.
Should not have
• Colorful patterns or excessive info in section 1B.

```html
<!DOCTYPE html>
<html lang="en">
<head>
<meta charset="utf-8">
<title>Saffron Meadow – Clear Skin Body Polish Label</title>
<link href="https://fonts.googleapis.com/css2?family=Special+Elite&family=Raleway:wght@300;400&family=Handlee&display=swap" rel="stylesheet">
<style>
  :root {
    --label-black: #262626;
    --gold: #f3d221;
    --white: #ffffff;
    --paper: #ffffff;
  }
  * { box-sizing: border-box; margin: 0; padding: 0; }
  html, body {
    width: 1200px;
    height: 298px;
    overflow: hidden;
    background: var(--paper);
  }
  .label {
    position: absolute;
    left: 24px;
    top: 58px;
    width: 1152px;
    height: 182px;
    background: var(--label-black);
    border-top: 8px solid var(--gold);
    border-bottom: 8px solid var(--gold);
    color: var(--white);
    overflow: hidden;
  }

  /* Left panel: claims and usage */
  .claims {
    position: absolute;
    left: 22px;
    top: 4px;
    width: 306px;
    height: 42px;
    table-layout: fixed;
    border-collapse: collapse;
    font-family: "Special Elite", "Courier New", monospace;
    font-size: 6.6px;
    letter-spacing: -0.4px;
    line-height: 1.3;
    border: 1px solid var(--white);
  }
  .claims td {
    border: 1px solid var(--white);
    text-align: center;
    vertical-align: middle;
    padding: 0 2px;
  }
  .claims .claim-cruelty { width: 74px; }
  .claims .claim-organic { width: 90px; }
  .claims .claim-free { text-align: left; vertical-align: top; padding-top: 5px; padding-left: 6px; }
  .usage {
    position: absolute;
    left: 13px;
    width: 320px;
    font-family: "Special Elite", "Courier New", monospace;
    font-size: 6.8px;
    letter-spacing: -0.5px;
    line-height: 9.2px;
    text-align: center;
    white-space: nowrap;
  }
  .usage-directions { top: 62px; }
  .usage-caution { top: 123px; }
  .usage-recycle { top: 154px; }

  /* Centre panel: brand */
  .brand-name {
    position: absolute;
    left: 406px;
    top: 12px;
    width: 252px;
    font-family: "Raleway", sans-serif;
    font-weight: 300;
    font-size: 26px;
    letter-spacing: 0.3px;
    color: var(--gold);
    white-space: nowrap;
  }
  .brand-mark {
    position: absolute;
    left: 392px;
    top: 64px;
    width: 96px;
    height: 96px;
    border-radius: 50%;
    background: var(--gold);
  }
  .product-name {
    position: absolute;
    left: 502px;
    top: 62px;
    width: 180px;
    font-family: "Raleway", sans-serif;
    font-weight: 400;
    font-size: 21px;
    line-height: 28px;
    text-align: center;
    white-space: nowrap;
  }
  .net-weight {
    position: absolute;
    left: 514px;
    top: 135px;
    width: 156px;
    height: 28px;
  }
  .net-weight svg { position: absolute; left: 0; top: 0; }
  .net-weight span {
    position: absolute;
    top: 8px;
    width: 40px;
    text-align: center;
    font-family: "Raleway", sans-serif;
    font-size: 10.5px;
  }
  .net-weight .unit-oz { left: 12px; }
  .net-weight .unit-grams { left: 98px; }

  /* Right panel: sideways story and ingredients, read bottom to top */
  .story {
    position: absolute;
    left: 720px;
    top: 160px;
    width: 146px;
    height: 320px;
    transform-origin: 0 0;
    transform: rotate(-90deg);
    font-family: "Handlee", cursive;
    font-size: 7.3px;
    line-height: 8px;
  }
  .story p { margin-bottom: 7px; }
  .story strong { font-weight: 700; }
</style>
</head>
<body>
  <main class="label">
    <table class="claims">
      <tr>
        <td class="claim-cruelty">Cruelty Free<br>Never Tested on<br>Animals</td>
        <td class="claim-organic">Organic Ingredients</td>
        <td class="claim-free">FREE OF:&nbsp; Parabens, Synthetics,<br>Fragrance, GMOs, or any other<br>fakeness.</td>
      </tr>
    </table>

    <p class="usage usage-directions">Directions: Shake well before use. Gently massage scrub in circular motions<br>over wet skin (not face). Pay special attention to rough or dry patches. After<br>use, a residual layer of oil will remain on skin. Rinse thoroughly and pat dry<br>with towel. Skin will feel elegantly soft and nourished. Avoid use on freshly<br>shaven or broken skin.</p>
    <p class="usage usage-caution">Caution: Oils in product may leave shower or tub surfaces slippery. Not<br>intended for facial use. Essential oils or use on freshly shaven skin may cause<br>skin irritation. External use only.</p>
    <p class="usage usage-recycle">Please recycle. I want to come back as a solar panel</p>

    <h1 class="brand-name">SAFFRON MEADOW</h1>
    <div class="brand-mark" role="img" aria-label="Brand mark area in gold"></div>
    <h2 class="product-name">Clear Skin<br>Body Polish</h2>

    <div class="net-weight">
      <svg width="156" height="28" viewBox="0 0 156 28" aria-hidden="true">
        <line x1="0" y1="0.5" x2="156" y2="0.5" stroke="#ffffff" stroke-width="1"/>
        <line x1="77.5" y1="0" x2="77.5" y2="28" stroke="#ffffff" stroke-width="1"/>
      </svg>
      <span class="unit-oz">oz</span>
      <span class="unit-grams">grams</span>
    </div>

    <section class="story">
      <p>Made with naturally derived ingredients only.</p>
      <p><strong>The combination of ingredients in this loving scrub were chosen with problematic body skin in mind.</strong> The high concentration of magnesium in Dead Sea Salt is instrumental in improving skin hydration and reducing inflammation.</p>
      <p>Pink salt is readily absorbed into the skin, cleansing and purifying the pores from the inside out. It can improve the texture, tone, and appearance of the skin.</p>
      <p>This loving essential oil concoction helps fight acne by removing toxins and draining sebaceous glands. Some EOs contain strong antibacterial, antifungal, and anti inflammatory properties. Certain EOs inhibit the bacteria that cause skin infections as well as target acne scarring and pigmentation from previous breakouts.</p>
      <p><strong>Each of these ingredients plays an essential role in anti aging, as well as fighting problematic skin. Use this skin polish regularly to receive prime results.</strong></p>
      <p><strong>Ingredients:</strong> Dead Sea Salt, Pink Himalayan Salt, Coconut oil, Argan Oil, Jojoba Oil, Almond Oil, Lavender EO, Tea Tree EO, Geranium EO, Chamomile EO, Bergamot EO, Frankincense EO, Rosemary EO.</p>
    </section>
  </main>
</body>
</html>
```